FC Morlan - Creation of a AD banner for our yearly event

We are a local soccer club in Switzerland. We're organizing a event that will substitute to our yearly club dinner. We need a banner AD to promote on the social networks this event.
We would like to see design that use one or the 2 colors of the club (blue and red).
This Ad should link to a online shop where we can buy vouchers.

Requirements
Must have
• Logo of the club
Title : Fête des lanternes d'hiver
Call to action : Plus d'informations
Side texte : Grande Tombola
Banner size : W300xH250 or W300xH600
Nice to have
• Promotion texte: Soutenez le FC Morlan et les restaurateurs locaux

```html
<!DOCTYPE html>
<html lang="fr">
<head>
<meta charset="utf-8">
<title>FC Morlan – Fête des lanternes d'hiver</title>
<link rel="stylesheet" href="https://fonts.googleapis.com/css2?family=Roboto+Condensed:wght@400;500;700&display=swap">
<style>
  :root {
    --club-red: #c9413d;
    --club-blue: #5089cb;
    --ink: #0d0d0d;
    --paper: #ffffff;
    --ball-tone: #e6e6e6;
  }
  html, body {
    margin: 0;
    width: 1200px;
    height: 1013px;
    overflow: hidden;
    background: var(--paper);
    font-family: "Roboto Condensed", "Arial Narrow", sans-serif;
  }
  .canvas { position: relative; width: 1200px; height: 1013px; }
  .banner { position: absolute; }
  .block {
    position: absolute;
    color: var(--paper);
    font-weight: 500;
    box-sizing: border-box;
    display: flex;
    align-items: center;
  }
  .block--title { background: var(--club-red); }
  .block--raffle { background: var(--club-blue); }
  .ball-deco {
    position: absolute;
    border-radius: 50%;
    background: radial-gradient(circle at 45% 40%, #f7f7f7 0%, var(--ball-tone) 70%, #d9d9d9 100%);
    opacity: 0.7;
  }
  .club-name {
    position: absolute;
    display: flex;
    align-items: center;
    color: var(--club-blue);
    font-weight: 700;
    white-space: nowrap;
  }
  .club-name .mark { background: var(--club-red); flex: none; }
  .promo {
    position: absolute;
    color: var(--club-blue);
    font-weight: 500;
    line-height: 1.15;
  }
  .cta {
    position: absolute;
    background: var(--ink);
    color: var(--paper);
    font-weight: 500;
    display: flex;
    align-items: center;
    justify-content: center;
  }

  /* 300 x 250 */
  .banner--rect { left: 110px; top: 339px; width: 414px; height: 346px; }
  .banner--rect .block--title { left: 0; top: 0; width: 204px; height: 171px; padding: 0 14px; font-size: 33px; line-height: 1.12; }
  .banner--rect .block--raffle { left: 212px; top: 0; width: 202px; height: 171px; padding: 0 42px; font-size: 33px; line-height: 1.2; }
  .banner--rect .ball-deco { left: 275px; top: 178px; width: 145px; height: 145px; }
  .banner--rect .club-name { left: 46px; top: 196px; font-size: 30px; gap: 8px; }
  .banner--rect .club-name .mark { width: 22px; height: 22px; }
  .banner--rect .promo { left: 175px; top: 226px; width: 240px; font-size: 18px; }
  .banner--rect .cta { left: 204px; top: 318px; width: 210px; height: 28px; font-size: 16px; }

  /* 300 x 600 */
  .banner--tall { left: 657px; top: 85px; width: 416px; height: 830px; }
  .banner--tall .block--title { left: 0; top: 0; width: 416px; height: 289px; padding: 0 58px; font-size: 62px; line-height: 1.08; }
  .banner--tall .block--raffle { left: 0; top: 298px; width: 416px; height: 287px; padding: 0 58px; font-size: 62px; line-height: 1.25; }
  .banner--tall .ball-deco { left: 196px; top: 592px; width: 228px; height: 228px; }
  .banner--tall .club-name { left: 12px; top: 600px; font-size: 38px; gap: 10px; }
  .banner--tall .club-name .mark { width: 28px; height: 28px; }
  .banner--tall .promo { left: 183px; top: 643px; width: 240px; font-size: 22px; }
  .banner--tall .cta { left: 183px; top: 780px; width: 233px; height: 50px; font-size: 21px; }
</style>
</head>
<body>
<main class="canvas">

  <section class="banner banner--rect" aria-label="Bannière 300 x 250">
    <div class="block block--title">Fête des lanternes d'hiver</div>
    <div class="block block--raffle">Grande Tombola</div>
    <div class="ball-deco" role="img" aria-label="Ballon de football en filigrane"></div>
    <div class="club-name"><span class="mark"></span>FC Morlan</div>
    <p class="promo">Soutenez le FC Morlan et les restaurateurs locaux</p>
    <a class="cta">Plus d'informations</a>
  </section>

  <section class="banner banner--tall" aria-label="Bannière 300 x 600">
    <div class="block block--title">Fête des lanternes d'hiver</div>
    <div class="block block--raffle">Grande Tombola</div>
    <div class="ball-deco" role="img" aria-label="Ballon de football en filigrane"></div>
    <div class="club-name"><span class="mark"></span>FC Morlan</div>
    <p class="promo">Soutenez le FC Morlan et les restaurateurs locaux</p>
    <a class="cta">Plus d'informations</a>
  </section>

</main>
</body>
</html>
```